Corvanto Card

The logo is the Spanish flag colors I want a vibrant eye catching design with the yellow / red colors over either Navy or white background or black even ,
Would like a 2D feel to the logo with another lighter color logo under it look ,

Contact Information for Business Card

Corvanto Flooring
Tobias Renwick
Main Number
Cell Number
Fax Number

Website on the side of the card somewhere

Font styles to use
Sans Serif

Colors
ec1f27
ffc214

Requirements
Must have
• 2 logos feel one is bolder and the other one underneath very light

```html
<!DOCTYPE html>
<html lang="en">
<head>
<meta charset="utf-8">
<title>Corvanto Flooring – Business Card</title>
<link rel="stylesheet" href="https://fonts.googleapis.com/css2?family=Archivo+Black&family=Arimo:wght@400;700&display=swap">
<style>
  :root {
    --red: #ec1f27;
    --yellow: #ffc214;
    --card: #1a1a1a;
    --backdrop: #2b2624;
    --text: #ffffff;
    --rule: #4a4a4a;
  }
  * { margin: 0; padding: 0; box-sizing: border-box; }
  html, body { width: 1200px; height: 842px; overflow: hidden; background: var(--backdrop); }
  .sheet { position: relative; width: 1200px; height: 842px; }

  .card {
    position: absolute;
    top: 266px;
    width: 540px;
    height: 309px;
    background: var(--card);
    overflow: hidden;
  }
  .card--contact { left: 40px; }
  .card--brand { left: 620px; }

  /* contact side */
  .band { position: absolute; left: 0; width: 100%; height: 18px; }
  .band--top { top: 0; background: var(--red); }
  .band--bottom { bottom: 0; background: var(--yellow); }

  .contact {
    position: absolute;
    top: 70px;
    left: 0;
    width: 100%;
    text-align: center;
    font-family: "Arimo", sans-serif;
    color: var(--text);
  }
  .person {
    font-family: "Archivo Black", sans-serif;
    font-size: 24px;
    letter-spacing: 1px;
    text-transform: uppercase;
  }
  .person__first { color: var(--red); }
  .person__last { color: var(--yellow); }
  .rule { width: 120px; height: 1px; background: var(--rule); margin: 12px auto; }
  .phones { list-style: none; font-size: 16px; line-height: 21px; }
  .phones__label { color: var(--red); font-weight: 700; }
  .web { font-size: 16px; line-height: 21px; }
  .web__site { color: var(--yellow); }
  .web__site span { color: var(--red); }

  /* brand side */
  .accent { position: absolute; display: flex; height: 52px; }
  .accent__red { width: 30px; background: var(--red); }
  .accent__gap { width: 4px; }
  .accent__yellow { width: 7px; background: var(--yellow); }
  .accent--left { left: 0; top: 150px; }
  .accent--right { right: 0; top: 62px; flex-direction: row-reverse; }

  .brand {
    position: absolute;
    top: 96px;
    left: 0;
    width: 100%;
    text-align: center;
    font-family: "Archivo Black", sans-serif;
    text-transform: uppercase;
  }
  .brand__mark {
    display: inline-block;
    width: 22px;
    height: 22px;
    background: var(--red);
    margin-bottom: 14px;
  }
  .brand__name {
    color: var(--red);
    font-size: 38px;
    line-height: 1;
    letter-spacing: 1px;
  }
  .brand__trade {
    color: var(--yellow);
    font-size: 20px;
    letter-spacing: 14px;
    margin-top: 12px;
    padding-left: 14px;
  }
</style>
</head>
<body>
<main class="sheet">
  <section class="card card--contact" aria-label="Contact side">
    <div class="band band--top"></div>
    <div class="contact">
      <h1 class="person"><span class="person__first">Tobias</span> <span class="person__last">Renwick</span></h1>
      <div class="rule"></div>
      <ul class="phones">
        <li><span class="phones__label">P:</span> 410 555 0182</li>
        <li><span class="phones__label">M:</span> 410 555 0247</li>
        <li><span class="phones__label">F:</span> 410 555 0390</li>
      </ul>
      <div class="rule"></div>
      <p class="web">hello@corvantoflooring.com</p>
      <p class="web web__site"><span>www.</span>corvantoflooring<span>.com</span></p>
    </div>
    <div class="band band--bottom"></div>
  </section>

  <section class="card card--brand" aria-label="Brand side">
    <div class="accent accent--left"><div class="accent__red"></div><div class="accent__gap"></div><div class="accent__yellow"></div></div>
    <div class="accent accent--right"><div class="accent__red"></div><div class="accent__gap"></div><div class="accent__yellow"></div></div>
    <div class="brand">
      <span class="brand__mark"></span>
      <p class="brand__name">Corvanto</p>
      <p class="brand__trade" style="color: var(--red);">Flooring</p>
    </div>
  </section>
</main>
</body>
</html>
```